Non-Fiction Book Cover Series Concepts

I need front cover concepts for a non-fiction business book series. Just concepts at this stage to show to backers (full cover designs later).

The books are for leaders and business owners. A mature, sophisticated market, AND, bold and innovative.

The series needs to be extensible - the concepts need to be able to work across at least 40 books. I am happy with a colour theme, or contrasts, or icon theme, there is no limitation to the imagination.

The books need to look like they belong to a series and to also stand alone.

I prefer simple and bold.

Imagine the Heron business series (https://www.heronbooks-example.co.uk/series/lbs/heron-leaders-masters-series.html) - but I hate these designs (the colours don't work for me).

The imprint is ThoughtfulHorizon.example - the logo mark for the imprint is attached.

The books will be printed and ebooks - the printed version will be 5 inches by 8 inches form factor. They will be printed with a matt cover.

IF YOU WANT A BOOK TITLE TO TRY, use this:

Steady Momentum: Apply the R.A.F. Model to Nurture, Unlock and Keep Talent

Thank you for your interest!

Target Market(s)

Business owners, leaders, entrepreneurs

Industry/Entity Type

Leadership

Font styles to use
Serif
Sans Serif

Requirements
Must have
• Extensible - the concept can work for many books and ALL books look part of the series
Nice to have
• I prefer simple, icons rather than photos
Should not have
• No photographic designs - icon, drawing

```html
<!DOCTYPE html>
<html lang="en">
<head>
<meta charset="UTF-8">
<title>Business Book Series – Cover Concepts</title>
<link rel="stylesheet" href="https://fonts.googleapis.com/css2?family=Nunito+Sans:wght@800;900&family=Montserrat:wght@300;500;600&display=swap">
<style>
  :root {
    --stage: #e2e2e2;
    --paper: #f1f1f1;
    --ink: #050505;
    --muted: #8a8a8a;
    --teal: #5b9a8c;
    --teal-light: #7ab8ab;
    --navy: #1f3d57;
    --navy-deep: #0f2434;
    --orange: #ec935b;
    --peach: #f0bb7f;
    --cream: #f3cf9c;
  }
  * { box-sizing: border-box; margin: 0; padding: 0; }
  html, body {
    width: 1200px; height: 888px; overflow: hidden;
    background: var(--stage);
  }
  .stage { position: relative; width: 1200px; height: 888px; }

  .cover {
    position: absolute; top: 109px;
    width: 478px; height: 670px;
    background: var(--paper);
    box-shadow: 0 6px 22px rgba(0,0,0,0.12);
    overflow: hidden;
  }
  .cover--teal { left: 91px; }
  .cover--orange { left: 627px; }

  .artwork { position: absolute; left: 0; width: 100%; }
  .cover--teal .artwork {
    top: 279px; height: 312px;
    background: linear-gradient(135deg, var(--teal-light) 0%, var(--navy) 45%, var(--teal) 70%, var(--navy) 100%);
  }
  .cover--orange .artwork {
    top: 0; height: 309px;
    background: linear-gradient(120deg, var(--peach) 0%, var(--cream) 40%, var(--orange) 75%, var(--peach) 100%);
  }

  .imprint { position: absolute; display: flex; align-items: flex-end; }
  .imprint__bar { width: 3px; height: 33px; }
  .cover--teal .imprint { left: 20px; top: 17px; }
  .cover--teal .imprint__bar { background: var(--teal); }
  .cover--orange .imprint { left: 31px; top: 330px; }
  .cover--orange .imprint__bar { background: var(--orange); }
  .imprint__name {
    margin-left: 13px; margin-bottom: -2px;
    font-family: "Montserrat", sans-serif; font-weight: 600;
    font-size: 6px; color: var(--ink);
  }

  .cover-label {
    position: absolute; right: 19px;
    font-family: "Montserrat", sans-serif; font-size: 8.5px;
    color: var(--muted); font-weight: 300;
  }
  .cover-label strong { font-weight: 600; color: #222; }
  .cover--teal .cover-label { top: 18px; }
  .cover--orange .cover-label { top: 317px; right: 27px; }

  .title {
    position: absolute; left: 27px;
    font-family: "Nunito Sans", sans-serif; font-weight: 900;
    font-size: 40px; line-height: 37px; letter-spacing: -0.3px;
    color: var(--ink);
  }
  .cover--teal .title { top: 103px; }
  .cover--orange .title { top: 455px; left: 28px; }

  .author {
    position: absolute;
    font-family: "Nunito Sans", sans-serif; font-weight: 900;
    font-size: 35px; letter-spacing: 0.2px;
    color: var(--ink); line-height: 1;
  }
  .cover--teal .author { left: 20px; top: 229px; }
  .cover--orange .author { left: 24px; top: 412px; }

  .blurb {
    position: absolute; top: 624px; right: 19px;
    font-family: "Montserrat", sans-serif; font-weight: 300;
    font-size: 7px; line-height: 8px; text-align: right;
    color: #6a6a6a;
  }
  .cover--orange .blurb { right: 27px; }
</style>
</head>
<body>
<main class="stage">

  <article class="cover cover--teal">
    <div class="imprint">
      <span class="imprint__bar"></span>
      <span class="imprint__name">ThoughtfulHorizon.example</span>
    </div>
    <p class="cover-label"><strong>Cover</strong> design</p>
    <h1 class="title">Non-Fiction<br>Business<br>Book Series</h1>
    <p class="author">AUTHOR’S NAME</p>
    <div class="artwork" role="img" aria-label="Geometric pattern of overlapping circles and diagonal bands in teal and navy"></div>
    <p class="blurb">Lorem ipsum dolor sit amet, consectetuer<br>Ut wisi enim ad minim veniam</p>
  </article>

  <article class="cover cover--orange">
    <div class="artwork" role="img" aria-label="Geometric pattern of rings, circles and diagonal bands in orange, peach and cream"></div>
    <p class="cover-label"><strong>Cover</strong> design</p>
    <div class="imprint">
      <span class="imprint__bar"></span>
      <span class="imprint__name">ThoughtfulHorizon.example</span>
    </div>
    <p class="author">AUTHOR’S NAME</p>
    <h1 class="title">Non-Fiction<br>Business<br>Book Series</h1>
    <p class="blurb">Lorem ipsum dolor sit amet, consectetuer<br>Ut wisi enim ad minim veniam</p>
  </article>

</main>
</body>
</html>
```